Construction APP

We need to design a modern app IOS/Android where my team can create a profile with their info, (maybe share some pictures), reviews, submit time cards, show their availability, etc.

Like a taxi app but for construction. We also want to be able to assign each team member to a project manager with who they currently working. So we will also need to be able to create profiles at the Administration level.

The goal is to keep innovating the app as we grow, so we are always open to suggestions and ideas.

Low design quality

Industry/Entity Type

Construction

Colors
FFC000
F8CF3A
FAE287
FDF2CF
FEFAEE

Requirements
Must have
• IOS/Android APP where my team can create a profile with their info, (maybe share some pictures), reviews, submit time cards, show their availability, etc.We also want to be able to assign each team member to a project manager with who they currently working. So we will also need to be able to create profiles at the Administration level.

```html
<!DOCTYPE html>
<html lang="en">
<head>
<meta charset="utf-8">
<title>Timesheets</title>
<link rel="stylesheet" href="https://fonts.googleapis.com/css2?family=Oswald:wght@400;500;600&family=Roboto+Condensed:wght@400;700&display=swap">
<style>
  :root {
    --ink: #121212;
    --header: #111111;
    --gold: #C4964C;
    --white: #ffffff;
    --muted: #6f6f6f;
    --nav-muted: #8a8a8a;
    --shadow: rgba(0, 0, 0, 0.14);
  }
  * { box-sizing: border-box; margin: 0; padding: 0; }
  html, body { width: 1200px; height: 2392px; overflow: hidden; }
  body {
    position: relative;
    background: var(--header);
    font-family: "Roboto Condensed", "Arial Narrow", sans-serif;
    color: var(--ink);
  }

  .app-header { position: absolute; inset: 0 0 auto 0; height: 520px; background: var(--header); }
  .app-title {
    position: absolute; left: 140px; top: 200px;
    font-family: "Oswald", sans-serif; font-weight: 500; font-size: 80px;
    letter-spacing: 1px; color: var(--white); line-height: 1;
  }
  .filter-button { position: absolute; right: 120px; top: 218px; width: 72px; height: 60px; }
  .tabs { position: absolute; left: 140px; top: 350px; display: flex; gap: 60px; }
  .tab {
    font-family: "Oswald", sans-serif; font-size: 50px; font-weight: 400;
    color: var(--white); padding: 0 10px 26px; line-height: 1;
  }
  .tab--active { color: var(--gold); font-weight: 500; border-bottom: 6px solid var(--gold); }

  .content-panel {
    position: absolute; left: 0; right: 0; top: 500px; bottom: 0;
    background: var(--white); border-radius: 90px 90px 0 0;
  }
  .project-name {
    position: absolute; left: 140px; top: 120px;
    font-family: "Oswald", sans-serif; font-weight: 500; font-size: 60px; line-height: 1;
    letter-spacing: 0.5px;
  }
  .project-date {
    position: absolute; left: 140px; top: 196px;
    font-family: "Oswald", sans-serif; font-size: 48px; color: #333; line-height: 1;
  }

  .timecard {
    position: absolute; left: 100px; width: 1000px; height: 450px;
    background: var(--white); border-radius: 18px;
    box-shadow: 0 10px 40px var(--shadow);
  }
  .timecard__title {
    position: absolute; left: 50px; top: 50px;
    font-family: "Oswald", sans-serif; font-weight: 500; font-size: 40px; line-height: 1;
  }
  .timecard__range {
    position: absolute; left: 50px; top: 102px; font-size: 23px; color: var(--muted);
  }
  .timecard__chevron { position: absolute; right: 60px; top: 56px; width: 30px; height: 40px; }
  .crew-avatar {
    position: absolute; left: 50px; top: 190px; width: 180px; height: 180px;
    border-radius: 50%; background: radial-gradient(circle at 50% 45%, #d3a864, var(--gold));
  }
  .crew-count {
    position: absolute; right: -8px; top: 0; width: 50px; height: 50px; border-radius: 50%;
    background: var(--ink); color: var(--white); font-size: 24px; font-weight: 700;
    display: flex; align-items: center; justify-content: center;
  }
  .hours { position: absolute; left: 300px; right: 40px; top: 218px; display: flex; }
  .hours__cell { flex: 1; text-align: center; }
  .hours__label {
    height: 40px; display: flex; align-items: center; justify-content: center;
    font-family: "Oswald", sans-serif; font-size: 28px; font-weight: 500;
  }
  .hours__value {
    margin-top: 14px; font-family: "Oswald", sans-serif; font-weight: 500; font-size: 56px; line-height: 1;
  }

  .tab-bar {
    position: absolute; left: 0; right: 0; bottom: 0; height: 230px;
    background: var(--white); border-radius: 70px 70px 0 0;
    box-shadow: 0 -8px 30px var(--shadow);
    display: flex; justify-content: space-around; padding: 40px 70px 0;
  }
  .tab-bar__item { width: 180px; text-align: center; color: var(--nav-muted); }
  .tab-bar__item svg { width: 64px; height: 64px; display: block; margin: 0 auto 18px; }
  .tab-bar__label { font-size: 26px; font-weight: 700; }
  .tab-bar__item--active { color: var(--gold); }
  .tab-bar__item--active .tab-bar__label { color: var(--gold); }
</style>
</head>
<body>
  <header class="app-header">
    <h1 class="app-title">TIMESHEETS</h1>
    <svg class="filter-button" viewBox="0 0 72 60" fill="none" stroke="#fff" stroke-width="5" stroke-linecap="round">
      <line x1="4" y1="14" x2="40" y2="14"/><circle cx="54" cy="14" r="9"/>
      <line x1="32" y1="46" x2="68" y2="46"/><circle cx="18" cy="46" r="9"/>
    </svg>
    <nav class="tabs">
      <span class="tab tab--active">Today</span>
      <span class="tab">Upcoming</span>
    </nav>
  </header>

  <main class="content-panel">
    <h2 class="project-name">HARBOR LANE RECONSTRUCTION</h2>
    <p class="project-date">September 3, 2021</p>

    <article class="timecard" style="top:290px">
      <h3 class="timecard__title">MULTIPLE PROJECTS</h3>
      <p class="timecard__range">Wed September 01, 2019 : 9:00 AM - 5:00 PM</p>
      <svg class="timecard__chevron" viewBox="0 0 30 40" fill="none" stroke="#121212" stroke-width="5"><polyline points="6,4 24,20 6,36"/></svg>
      <div class="crew-avatar" role="img" aria-label="Illustrated construction worker avatar"><span class="crew-count">7</span></div>
      <div class="hours">
        <div class="hours__cell"><div class="hours__label">ST</div><div class="hours__value">8:00</div></div>
        <div class="hours__cell"><div class="hours__label">OT</div><div class="hours__value">2:00</div></div>
        <div class="hours__cell"><div class="hours__label">DT</div><div class="hours__value">1:00</div></div>
        <div class="hours__cell"><div class="hours__label"><svg width="34" height="34" viewBox="0 0 34 34" fill="none" stroke="#121212" stroke-width="3.5"><circle cx="17" cy="17" r="14"/><polyline points="17,9 17,17 23,20"/></svg></div><div class="hours__value">11:00</div></div>
      </div>
    </article>

    <article class="timecard" style="top:790px">
      <h3 class="timecard__title">48 CEDAR ROW</h3>
      <p class="timecard__range">Wed September 01, 2019 : 9:00 AM - 5:00 PM</p>
      <svg class="timecard__chevron" viewBox="0 0 30 40" fill="none" stroke="#121212" stroke-width="5"><polyline points="6,4 24,20 6,36"/></svg>
      <div class="crew-avatar" role="img" aria-label="Illustrated construction worker avatar"><span class="crew-count">1</span></div>
      <div class="hours">
        <div class="hours__cell"><div class="hours__label">ST</div><div class="hours__value">8:00</div></div>
        <div class="hours__cell"><div class="hours__label">OT</div><div class="hours__value">2:00</div></div>
        <div class="hours__cell"><div class="hours__label">DT</div><div class="hours__value">1:00</div></div>
        <div class="hours__cell"><div class="hours__label"><svg width="34" height="34" viewBox="0 0 34 34" fill="none" stroke="#121212" stroke-width="3.5"><circle cx="17" cy="17" r="14"/><polyline points="17,9 17,17 23,20"/></svg></div><div class="hours__value">11:00</div></div>
      </div>
    </article>

    <article class="timecard" style="top:1290px">
      <h3 class="timecard__title">MULTIPLE PROJECTS</h3>
      <p class="timecard__range">Wed September 01, 2019 : 9:00 AM - 5:00 PM</p>
      <svg class="timecard__chevron" viewBox="0 0 30 40" fill="none" stroke="#121212" stroke-width="5"><polyline points="6,4 24,20 6,36"/></svg>
      <div class="crew-avatar" role="img" aria-label="Illustrated construction worker avatar"><span class="crew-count">7</span></div>
      <div class="hours">
        <div class="hours__cell"><div class="hours__label">ST</div><div class="hours__value">8:00</div></div>
        <div class="hours__cell"><div class="hours__label">OT</div><div class="hours__value">2:00</div></div>
        <div class="hours__cell"><div class="hours__label">DT</div><div class="hours__value">1:00</div></div>
        <div class="hours__cell"><div class="hours__label"><svg width="34" height="34" viewBox="0 0 34 34" fill="none" stroke="#121212" stroke-width="3.5"><circle cx="17" cy="17" r="14"/><polyline points="17,9 17,17 23,20"/></svg></div><div class="hours__value">11:00</div></div>
      </div>
    </article>

    <nav class="tab-bar">
      <div class="tab-bar__item tab-bar__item--active">
        <svg viewBox="0 0 64 64" fill="none" stroke="currentColor" stroke-width="4"><rect x="8" y="8" width="48" height="48" rx="10"/><circle cx="32" cy="32" r="12"/><polyline points="32,25 32,32 37,35"/></svg>
        <span class="tab-bar__label">Time Card</span>
      </div>
      <div class="tab-bar__item">
        <svg viewBox="0 0 64 64" fill="none" stroke="currentColor" stroke-width="4"><rect x="8" y="12" width="48" height="44" rx="6"/><line x1="8" y1="24" x2="56" y2="24"/><line x1="20" y1="6" x2="20" y2="16"/><line x1="44" y1="6" x2="44" y2="16"/><circle cx="22" cy="34" r="2"/><circle cx="32" cy="34" r="2"/><circle cx="42" cy="34" r="2"/><circle cx="22" cy="45" r="2"/><circle cx="32" cy="45" r="2"/></svg>
        <span class="tab-bar__label">Time View</span>
      </div>
      <div class="tab-bar__item">
        <svg viewBox="0 0 64 64" fill="none" stroke="currentColor" stroke-width="4"><path d="M14 6h26l12 12v40H14z"/><line x1="22" y1="32" x2="42" y2="32"/><line x1="22" y1="42" x2="38" y2="42"/></svg>
        <span class="tab-bar__label">Forms</span>
      </div>
      <div class="tab-bar__item">
        <svg viewBox="0 0 64 64" fill="none" stroke="currentColor" stroke-width="4"><rect x="8" y="8" width="48" height="48" rx="8"/><line x1="22" y1="44" x2="22" y2="32"/><line x1="32" y1="44" x2="32" y2="20"/><line x1="42" y1="44" x2="42" y2="28"/></svg>
        <span class="tab-bar__label">Productivity</span>
      </div>
      <div class="tab-bar__item">
        <svg viewBox="0 0 64 64" fill="none" stroke="currentColor" stroke-width="4"><circle cx="32" cy="22" r="12"/><path d="M12 58c0-12 9-20 20-20s20 8 20 20z"/></svg>
        <span class="tab-bar__label">Profile</span>
      </div>
    </nav>
  </main>
</body>
</html>
```